Business cards - KESTO Roofing & Siding

We need simple business cards made up for our Roofing & Siding business based in Calgary Alberta.
The logo on one side of the card and potentially our slogan "Built with trust, verified by time".
The other side could have:
-A small logo
-Rep name:
-Rep cell phone:
-Rep email:
-Office phone: 403-386-2049
-Website: PrairieShinglePros.com

We would like to incorporate the colours from our logo, especially the lite blue on the jpeg file. I have attached the ai file and jpeg file. We like the colours better on the jpeg file.

I do not require a money back guarantee

```html
<!DOCTYPE html>
<html lang="en">
<head>
<meta charset="utf-8">
<title>KESTO Roofing &amp; Siding — Business Cards</title>
<link rel="stylesheet" href="https://fonts.googleapis.com/css2?family=Montserrat:wght@400;500;700;800&display=swap">
<style>
  :root {
    --blue: #1167b8;
    --light-blue: #4a86c8;
    --ink: #1a1a1a;
    --grey-text: #444;
    --paper: #ffffff;
    --table: #4a4a4a;
  }
  * { box-sizing: border-box; margin: 0; padding: 0; }
  html, body { width: 1200px; height: 801px; overflow: hidden; }
  body {
    background: var(--table);
    font-family: "Montserrat", sans-serif;
    position: relative;
  }
  .card {
    position: absolute;
    top: 246px;
    width: 540px;
    height: 309px;
    background: var(--paper);
    border-bottom: 4px solid var(--blue);
    overflow: hidden;
  }
  .card--contact { left: 40px; }
  .card--logo { left: 620px; }

  /* Contact side */
  .contact-brand {
    position: absolute;
    left: 26px; top: 60px;
    width: 190px;
    display: flex; align-items: center; gap: 10px;
  }
  .brand-square {
    width: 18px; height: 18px;
    background: var(--light-blue);
    flex: none;
  }
  .brand-name {
    font-weight: 700;
    color: var(--ink);
    font-size: 17px;
    line-height: 1.2;
  }
  .divider {
    position: absolute;
    left: 226px; top: 30px;
    width: 1.5px; height: 180px;
    background: var(--blue);
  }
  .details {
    position: absolute;
    left: 244px; top: 28px;
    color: var(--ink);
    font-size: 12px;
    line-height: 1.45;
  }
  .rep-name {
    color: var(--blue);
    font-weight: 800;
    font-size: 19px;
    letter-spacing: 0.3px;
    line-height: 1.1;
  }
  .rep-title { font-size: 12.5px; margin-bottom: 10px; }
  .address { margin-bottom: 8px; }
  .contact-list { list-style: none; }
  .contact-list li { display: flex; align-items: center; gap: 6px; }
  .contact-list svg { width: 11px; height: 11px; fill: var(--blue); flex: none; }
  .slogan-band {
    position: absolute;
    left: 0; right: 0; top: 234px;
    height: 30px;
    background: var(--blue);
    color: var(--paper);
    font-size: 13px;
    display: flex; align-items: center; justify-content: center;
    letter-spacing: 0.3px;
  }

  /* Logo side */
  .logo-lockup {
    position: absolute;
    inset: 0;
    display: flex; align-items: center; justify-content: center; gap: 16px;
  }
  .logo-lockup .brand-square { width: 30px; height: 30px; }
  .logo-lockup .brand-name { font-size: 36px; }
</style>
</head>
<body>

<section class="card card--contact" aria-label="Business card, contact side">
  <div class="contact-brand">
    <span class="brand-square"></span>
    <span class="brand-name">KESTO Roofing &amp; Siding</span>
  </div>
  <div class="divider"></div>
  <div class="details">
    <p class="rep-name">DANIEL REYES</p>
    <p class="rep-title">Project Manager</p>
    <p class="address">2478 - 9 Avenue S.E. Calgary,<br>Alberta T2G 4M5</p>
    <ul class="contact-list">
      <li><svg viewBox="0 0 12 12"><path d="M3 0h6a1 1 0 0 1 1 1v10a1 1 0 0 1-1 1H3a1 1 0 0 1-1-1V1a1 1 0 0 1 1-1zm0 1.5v8h6v-8z"/></svg>123-456-7890</li>
      <li><svg viewBox="0 0 12 12"><path d="M1 3c2-3 8-3 10 0l-1 2-2-1V3H4v1L2 5zm2 3h6l1 5H2z"/></svg>403-386-2049</li>
      <li><svg viewBox="0 0 12 12"><path d="M0 2h12v8H0zm1 1v.5l5 3.5 5-3.5V3z"/></svg>info@kestomail.com</li>
      <li><svg viewBox="0 0 12 12"><circle cx="6" cy="6" r="6"/></svg>www.PrairieShinglePros.com</li>
    </ul>
  </div>
  <div class="slogan-band">Built with trust, verified by time</div>
</section>

<section class="card card--logo" aria-label="Business card, logo side">
  <div class="logo-lockup">
    <span class="brand-square"></span>
    <span class="brand-name">KESTO Roofing &amp; Siding</span>
  </div>
</section>

</body>
</html>
```